quillcrestPRESS is launching 2 new eBooks and needs beautiful and compelling cover designs and a desig

We are launching 2 non-fiction eBooks that are part of a series but will be launched separately, so we would like to see some continuity between the 2 designs - but each should have a strong stand alone identity.

The eBooks are both in the naturopathic/holistic health niche.

ebook 1 title is:
Shaping Your Perfect Studio
(sub) The Wellness Manual to growing your own thriving natural and
alternative therapy business.

The book is a comprehensive guide for naturopaths and other alternative health providers - ( Naturopath,
Nutritionist, Homeopath, Acupuncturist, Chiropractor,
Massage Therapist, or Holistic Health Specialist), who are seeking to setup their own, profitable naturopathic business.

ebook 2 title is:
Silver Handshakes (subtitle) Win 40 + Patients Inside Six Weeks

(sub/sub)27 methods to promote your natural and alternative therapy business

This book is a list of 32 tips for the same audience to increase there customer referrals (and therefore income).

Each book should feature
written by Moira Tennant
published by Tennant Publishing

Each book should feature the authors photograph on the cover (attached) - no caveats on cropping etc - whatever fits with the design.

You can see more about the writer on her website here:

http://www.harbourleafwellness.example.au/

What we require:

1) cover art for both eBooks that conforms to Kindle and iPad specs
2) Flat & 3D book cover art for use on website and marketing campaigns
3) we will require layered PSD files on completion of project.

I'd like to add that we are seeking to build a relationship with the designer we choose for this project, as we are publishing many other titles throughout 2014

Many eBook writers jump straight to Gigly for a cover. The result is most self published books have the same generic look the 'gigly' look.

I don't want that look.

We want to reward great design and ensure quillcrestPRESS eBook titles have a great look.

The winning designer will be working with us on many more projects.

Colin Marsh
quillcrestPRESS

```html
<!DOCTYPE html>
<html lang="en">
<head>
<meta charset="utf-8">
<title>Shaping Your Perfect Studio — Moira Tennant</title>
<link rel="stylesheet" href="https://fonts.googleapis.com/css2?family=Josefin+Sans:wght@300;400&family=Roboto+Slab:wght@500&display=swap">
<style>
  :root {
    --backdrop: #5ea320;
    --accent: #f78b1f;
    --paper: #ffffff;
    --ink-dark: #2b2b2b;
    --forest-light: #c9e98a;
    --forest-mid: #7cc23a;
    --forest-deep: #3f7a1c;
    --portrait-tone: #d9cfc6;
  }
  html, body {
    margin: 0;
    padding: 0;
    width: 1029px;
    height: 1200px;
    overflow: hidden;
    background: var(--backdrop);
  }
  .cover {
    position: absolute;
    left: 144px;
    top: 80px;
    width: 740px;
    height: 1040px;
    background: var(--paper);
    display: flex;
    flex-direction: column;
  }
  .author-band {
    height: 104px;
    background: var(--accent);
    display: flex;
    align-items: center;
    justify-content: center;
  }
  .author-name {
    margin: 0;
    font-family: "Josefin Sans", sans-serif;
    font-weight: 400;
    font-size: 46px;
    letter-spacing: 3px;
    color: var(--paper);
    text-transform: uppercase;
    padding-top: 8px;
  }
  .forest-scene {
    position: relative;
    height: 620px;
    background: radial-gradient(circle at 55% 30%, #f4fbe0 0%, var(--forest-light) 25%, var(--forest-mid) 60%, var(--forest-deep) 100%);
  }
  .author-portrait {
    position: absolute;
    left: 50%;
    top: 455px;
    width: 168px;
    height: 168px;
    margin-left: -96px;
    border: 12px solid var(--accent);
    border-radius: 50%;
    background: radial-gradient(circle at 50% 40%, #efe9e3 0%, var(--portrait-tone) 70%, #b9a99a 100%);
  }
  .title-panel {
    flex: 1;
    text-align: center;
    padding-top: 30px;
  }
  .book-title {
    margin: 0;
    font-family: "Josefin Sans", sans-serif;
    font-weight: 300;
    font-size: 60px;
    line-height: 60px;
    letter-spacing: 5px;
    color: var(--accent);
    text-transform: uppercase;
  }
  .book-subtitle {
    margin: 14px auto 0;
    width: 360px;
    font-family: "Roboto Slab", serif;
    font-weight: 500;
    font-size: 18px;
    line-height: 21px;
    color: var(--ink-dark);
  }
  .publisher-band {
    height: 46px;
    background: var(--accent);
    display: flex;
    align-items: center;
    justify-content: center;
  }
  .publisher-name {
    font-family: "Josefin Sans", sans-serif;
    font-weight: 400;
    font-size: 22px;
    color: var(--paper);
    padding-top: 4px;
  }
</style>
</head>
<body>
  <article class="cover">
    <header class="author-band">
      <p class="author-name">Moira Tennant</p>
    </header>
    <div class="forest-scene" role="img" aria-label="Sunlight streaming through a canopy of green forest trees">
      <div class="author-portrait" role="img" aria-label="Portrait photograph of the author"></div>
    </div>
    <section class="title-panel">
      <h1 class="book-title">Shaping<br>Your Perfect<br>Studio</h1>
      <p class="book-subtitle">The Wellness Manual to growing your own thriving natural and alternative therapy business</p>
    </section>
    <footer class="publisher-band">
      <span class="publisher-name">Tennant Publishing</span>
    </footer>
  </article>
</body>
</html>
```